Business Card Design - Crisp & Clean

Looking for a new clean and crisp business card design. Design must incorporate our corporate colors (see attached style sheet). We're a pretty fun loving group who likes to keep it light while still portraying a professional image. Card should incorporate both our logo and our mascot (see attachment). Card should be double sided and should have room for our social media - Gleamrow, Brisk Hub and Zumbly on the back. Font selections do not have to match the style guide.

```html
<!DOCTYPE html>
<html lang="en">
<head>
<meta charset="utf-8">
<title>Quillbrook HR – Business Card</title>
<link href="https://fonts.googleapis.com/css2?family=Roboto:wght@400;500&display=swap" rel="stylesheet">
<style>
  :root {
    --stage: #716658;
    --paper: #ffffff;
    --brand-yellow: #ffcc05;
    --brand-yellow-soft: #ffd83a;
    --ink: #4a4a4a;
    --ink-dark: #222222;
    --divider: #e2c766;
    --faint: #f1f1f3;
    --mascot-tone: #e9e4da;
  }
  * { margin: 0; padding: 0; box-sizing: border-box; }
  html, body {
    width: 1200px; height: 900px; overflow: hidden;
    background: var(--stage);
    font-family: "Roboto", Arial, sans-serif;
  }
  .canvas { position: relative; width: 1200px; height: 900px; }

  .card {
    position: absolute; left: 296px; width: 608px; height: 372px;
    background: var(--paper); overflow: hidden;
  }
  .card--front { top: 49px; }
  .card--back { top: 485px; }

  .front-face {
    position: absolute; left: 14px; top: 14px; width: 579px; height: 342px;
    background: var(--brand-yellow); overflow: hidden;
  }
  .mascot {
    position: absolute; left: 24px; top: 8px; width: 150px; height: 232px;
    border-radius: 60px 60px 20px 20px;
    background: linear-gradient(180deg, var(--mascot-tone) 0%, #d9d3c6 60%, #5a463a 100%);
    opacity: 0.9;
  }
  .brand-mark {
    position: absolute; display: flex; align-items: center; gap: 10px;
    font-weight: 500; white-space: nowrap;
  }
  .brand-mark__dot { width: 22px; height: 22px; border-radius: 50%; }
  .front-face .brand-mark { left: 306px; top: 52px; font-size: 30px; color: var(--paper); }
  .front-face .brand-mark__dot { background: var(--paper); }
  .front-deco {
    position: absolute; right: -60px; bottom: -50px; width: 200px; height: 200px;
    border-radius: 50%; background: var(--brand-yellow-soft);
  }

  .back-deco {
    position: absolute; right: -50px; bottom: -40px; width: 190px; height: 190px;
    border-radius: 50%; background: var(--faint);
  }
  .card--back .brand-mark { left: 50px; top: 166px; font-size: 30px; color: var(--ink-dark); }
  .card--back .brand-mark__dot { background: var(--brand-yellow); }

  .divider {
    position: absolute; left: 320px; top: 68px; width: 1px; height: 235px;
    background: var(--divider);
  }
  .contact { position: absolute; left: 349px; top: 70px; color: var(--ink); }
  .contact__name { font-size: 19px; line-height: 24px; }
  .contact__role { font-size: 14px; line-height: 18px; color: var(--brand-yellow); }
  .contact__lines { margin-top: 37px; font-size: 16px; line-height: 22px; }

  .social { position: absolute; left: 349px; top: 262px; display: flex; gap: 16px; }
  .social__item { display: flex; align-items: center; gap: 5px; font-size: 12px; color: var(--ink); }
  .social__item::before {
    content: ""; width: 12px; height: 12px; background: var(--ink); display: block;
  }
</style>
</head>
<body>
<main class="canvas">
  <section class="card card--front" aria-label="Card front">
    <div class="front-face">
      <div class="front-deco" aria-hidden="true"></div>
      <div class="mascot" role="img" aria-label="Company mascot: cheerful professor character pointing toward the logo"></div>
      <div class="brand-mark"><span class="brand-mark__dot"></span>Quillbrook HR</div>
    </div>
  </section>

  <section class="card card--back" aria-label="Card back">
    <div class="back-deco" aria-hidden="true"></div>
    <div class="brand-mark"><span class="brand-mark__dot"></span>Quillbrook HR</div>
    <div class="divider"></div>
    <div class="contact">
      <p class="contact__name">Maren Holt</p>
      <p class="contact__role">Marketing Wizard</p>
      <div class="contact__lines">
        <p>maren@quillbrookhr.com</p>
        <p>Mobile: 555-014-2298</p>
      </div>
    </div>
    <div class="social">
      <span class="social__item">Gleamrow</span>
      <span class="social__item">Zumbly</span>
      <span class="social__item">Brisk Hub</span>
    </div>
  </section>
</main>
</body>
</html>
```